School website design - Technology and the arts

We will need a new or updated design that incorporates the following features:
-Reactive design that changes with the needs of the device.
-Static Background - only content scrolls
-Static Menu - similar to the Pressly Harbor Lantern theme
-Alert box for important notices (closings/emergency use only) that doesn’t display unless active
-Margins must be wider than “standard pressly theme” (fits the entire display at any resolution, doesn’t just center a columned design)
-Features an image scroll on the front page to show our current works/progress. (only if the screen is big enough). Should have swipe capability
-We must have a place on the front page to display the current school news as well as a location to display current events with a poster (see current webdesign for example)
-Uses the school colors (green and gold/yellow) in a way that is pleasing to the eye.
-Unique design to our school that is very clean and modern.
-Events need to be able to pop-out when you mouseover in a desktop environment. Example: http://skinvault.example/category/pressly/creative (mouse over a theme and it shows additional information about it without a refresh)
-Custom Admin panel to easily updated the news and events section.
-Notes: We are currently using some free icons that we found to make the current site look not so boring since we do not have a lot of content on each page. We would like to step away from that and are open to suggestions. Possibly something like http://vormlab.example/demo/?theme=arch under the services section but smaller.
-Notes 2: We have plenty of pictures of our building and activities that can be used as a background, etc.
-We are open to new ideas and suggestions.

Our current website is https://www.kelmont-academy.example to get an idea on how we manage our current site.

```html
<!DOCTYPE html>
<html lang="en">
<head>
<meta charset="utf-8">
<title>Kelmont Regional Academy</title>
<link rel="stylesheet" href="https://fonts.googleapis.com/css2?family=Jost:wght@400;500;600;700&display=swap">
<style>
:root{
  --green:#0f6b2a;
  --green-dark:#0b4a1d;
  --green-btn:#13802f;
  --gold:#f7c200;
  --paper:#f6f2e8;
  --ink:#1c1c1c;
  --rule:#d9d3c4;
}
*{box-sizing:border-box;margin:0;padding:0}
html,body{width:877px;height:1200px;overflow:hidden}
body{font-family:"Jost",sans-serif;color:var(--ink);background:var(--paper);position:relative}
.abs{position:absolute}

/* page backdrop */
.backdrop{left:0;top:415px;width:877px;height:697px;
  background:
    radial-gradient(ellipse 260px 340px at 60px 420px,rgba(120,130,110,.18),transparent 70%),
    radial-gradient(ellipse 220px 320px at 830px 330px,rgba(120,130,110,.16),transparent 70%),
    radial-gradient(ellipse 380px 260px at 440px 300px,rgba(150,150,140,.14),transparent 70%),
    linear-gradient(180deg,#f7f4ec 0%,#efebe1 55%,#f5f1e8 100%)}

/* header */
.site-header{left:0;top:0;width:877px;height:98px;background:#fff}
.brand-mark{left:80px;top:8px;width:80px;height:80px;border-radius:50%;background:var(--gold);display:flex;align-items:center;justify-content:center;color:var(--green-dark);font-weight:600;font-size:14px}
.brand-title{left:178px;top:7px;color:var(--green);font-weight:500;font-size:25px;line-height:25px;letter-spacing:.3px}
.brand-tagline{left:181px;top:58px;font-size:7.5px;color:#444}
.search{left:619px;top:17px;width:163px;height:17px;border-radius:10px;background:#eee;border:1px solid #ccc;box-shadow:inset 0 1px 2px rgba(0,0,0,.15)}
.search-btn{right:2px;top:1px;width:38px;height:13px;border-radius:8px;background:var(--green-btn);color:#fff;font-size:7.5px;text-align:center;line-height:13px}
.utility{left:606px;top:50px;font-size:9px;color:#333}
.utility span{margin:0 8px;color:#999}
.main-nav{left:181px;top:72px;height:24px;display:flex;font-size:9.4px;font-weight:600;color:#111}
.main-nav a{padding:0 8.4px;line-height:24px;text-decoration:none;color:inherit}
.main-nav a.active{background:var(--green-btn);color:#fff;padding:0 9px}

/* hero */
.hero-band{left:0;top:98px;width:877px;height:317px;background:var(--gold)}
.hero-slide{left:77px;top:118px;width:724px;height:330px;box-shadow:0 8px 12px rgba(0,0,0,.28);
  background:
    radial-gradient(ellipse 150px 120px at 330px 90px,rgba(222,190,120,.85),transparent 70%),
    radial-gradient(ellipse 200px 170px at 340px 250px,rgba(110,112,108,.9),transparent 72%),
    radial-gradient(ellipse 120px 90px at 460px 40px,rgba(70,55,45,.75),transparent 70%),
    radial-gradient(ellipse 160px 130px at 560px 190px,rgba(250,250,248,.9),transparent 70%),
    linear-gradient(90deg,#b6ab98 0%,#9c9488 35%,#c9c5bd 60%,#e9e8e2 100%)}
.hero-caption{left:96px;top:226px;width:192px;height:192px;background:rgba(25,92,40,.93);box-shadow:6px 6px 0 rgba(225,225,220,.75);padding:40px 12px 0;color:#fff;font-weight:700;font-size:21px;line-height:26px}
.hero-dots{left:107px;top:429px;display:flex;gap:3px;z-index:2}
.hero-dots i{width:7px;height:7px;border-radius:50%;background:#444;border:1.5px solid #fff}
.hero-dots i:first-child{background:#fff}

/* welcome */
.welcome-title{left:0;top:468px;width:877px;text-align:center;color:var(--green-dark);font-weight:700;font-size:19px;letter-spacing:.4px}
.welcome-text{left:106px;top:499px;width:665px;text-align:center;font-size:13px;line-height:18px;color:#333}
.activity{top:552px;width:140px;text-align:center}
.activity-photo{width:140px;height:140px;border-radius:50%;border:2px solid #fff;box-shadow:0 2px 6px rgba(0,0,0,.3)}
.activity-label{margin-top:12px;color:var(--green-dark);font-size:14px;font-weight:500}
.btn{background:var(--green-btn);color:#fff;font-size:11px;font-weight:500;text-align:center;border-radius:2px;box-shadow:0 2px 3px rgba(0,0,0,.3)}
.btn-more{left:373px;top:728px;width:131px;height:24px;line-height:24px;letter-spacing:.5px}
.rule-h{left:95px;top:768px;width:687px;height:1px;background:var(--rule)}
.rule-v{left:535px;top:790px;width:1px;height:300px;background:var(--rule)}

/* news */
.section-title{font-weight:700;font-size:15px;color:#111;letter-spacing:.3px}
.news-photo{left:96px;top:822px;width:182px;height:100px;border:2px solid var(--gold);
  background:
    radial-gradient(ellipse 40px 50px at 45px 50px,rgba(230,200,150,.9),transparent 75%),
    radial-gradient(ellipse 50px 40px at 150px 70px,rgba(60,140,80,.85),transparent 75%),
    radial-gradient(ellipse 60px 40px at 100px 40px,rgba(120,150,190,.8),transparent 75%),
    linear-gradient(180deg,#b9c7d6 0%,#e4dccb 60%,#d0cbc0 100%)}
.news-heading{color:var(--green-dark);font-weight:600;font-size:12px;line-height:14px}
.news-text{font-size:9.5px;line-height:12.5px;color:#222;text-align:justify}
.btn-news{left:95px;top:1058px;width:86px;height:24px;line-height:24px}

/* events */
.event-date{left:563px;text-align:center;width:24px;color:#555}
.event-date b{display:block;font-size:10px;font-weight:600}
.event-date strong{display:block;font-size:18px;color:var(--green-dark);font-weight:700}
.event-time{font-size:9.5px;font-style:italic;margin:6px 0 4px}
.btn-events{left:564px;top:1040px;width:92px;height:24px;line-height:24px}

/* footer */
.site-footer{left:0;top:1112px;width:877px;height:88px;background:var(--green-dark);border-top:3px solid #0d5a22}
.copyright{left:0;top:1131px;width:877px;text-align:center;color:#fff;font-size:9.5px}
.social{left:393px;top:1157px;display:flex;gap:5px}
.social i{width:21px;height:21px;border-radius:50%;background:#2b56a3;border:2px solid #fff}
.social i:nth-child(2){background:#2aa4d8}
.social i:nth-child(3){background:#8b5a3c}
</style>
</head>
<body>

<div class="backdrop abs" role="img" aria-label="Faint sketch of the school building and trees"></div>

<header class="site-header abs">
  <div class="brand-mark abs">Kelmont</div>
  <h1 class="brand-title abs">KELMONT REGIONAL<br>ACADEMY</h1>
  <p class="brand-tagline abs">For the arts &amp; technology | 48 Harrow Lane, 10427 555.014.2290</p>
  <div class="search abs"><div class="search-btn abs">Search</div></div>
  <nav class="utility abs">KRA Email<span>|</span>Calendars<span>|</span>Contact Us</nav>
  <nav class="main-nav abs">
    <a class="active">HOME</a><a>ABOUT KRA</a><a>STUDENTS/PARENTS</a><a>FACULTY/STAFF</a><a>DOCUMENTS/FORMS</a><a>PROGRAMS OF STUDY</a><a>SERVICES</a>
  </nav>
</header>

<div class="hero-band abs"></div>
<div class="hero-slide abs" role="img" aria-label="Photo of students writing at desks in a classroom"></div>
<div class="hero-caption abs">WHERE<br>TALENT IS<br>DISCOVERED<br>AND<br>NURTURED.</div>
<div class="hero-dots abs"><i></i><i></i><i></i><i></i></div>

<h2 class="welcome-title abs">WELCOME TO UNLEASHING TALENT!</h2>
<p class="welcome-text abs">Lorem ipsum dolor sit amet, consectetuer adipiscing elit, sed diam nonummy nibh euismod tincidunt ut laoreet dolore magna aliquam erat volutpat. Ut wisi enim ad minim veniam, quis nostrud exerci tation ullamcorper.</p>

<div class="activity abs" style="left:119px"><div class="activity-photo" role="img" aria-label="Photo of students playing tennis" style="background:radial-gradient(circle at 60% 40%,#f4f2ee 0 20%,transparent 45%),radial-gradient(circle at 35% 70%,#c8d0b0 0 15%,transparent 40%),linear-gradient(160deg,#8a9aa2,#5d6a60 60%,#3f4a40)"></div><div class="activity-label">SPORTS</div></div>
<div class="activity abs" style="left:286px"><div class="activity-photo" role="img" aria-label="Photo of students painting in an art class" style="background:radial-gradient(circle at 30% 55%,#d24a2a 0 12%,transparent 30%),radial-gradient(circle at 62% 65%,#2f6fb0 0 14%,transparent 32%),radial-gradient(circle at 70% 35%,#e7c47a 0 14%,transparent 34%),linear-gradient(160deg,#b57a3a,#6a4524 70%,#3e2614)"></div><div class="activity-label">ART &amp; CRAFT</div></div>
<div class="activity abs" style="left:452px"><div class="activity-photo" role="img" aria-label="Photo of students playing guitar" style="background:radial-gradient(circle at 40% 55%,#c9b24a 0 16%,transparent 34%),radial-gradient(circle at 70% 50%,#2a2a2a 0 12%,transparent 30%),linear-gradient(160deg,#b99a62,#6d5430 65%,#3a2c18)"></div><div class="activity-label">MUSIC</div></div>
<div class="activity abs" style="left:619px"><div class="activity-photo" role="img" aria-label="Photo of dancers leaping" style="background:radial-gradient(circle at 50% 45%,#5a4a48 0 14%,transparent 34%),radial-gradient(circle at 50% 50%,#f4f8fa 0 30%,transparent 70%),linear-gradient(180deg,#cfe0e6,#86a5b0)"></div><div class="activity-label">DANCE</div></div>

<div class="btn btn-more abs">MORE &nbsp;ACTIVITIES</div>
<div class="rule-h abs"></div>
<div class="rule-v abs"></div>

<h3 class="section-title abs" style="left:95px;top:787px">NEWS UPDATES</h3>
<div class="news-photo abs" role="img" aria-label="Photo of students in a classroom"></div>
<div class="abs" style="left:292px;top:821px;width:213px">
  <h4 class="news-heading">Annual Cultural-cum-Sports</h4>
  <p class="news-text" style="margin-top:9px">Lorem ipsum dolor sit amet, consectetuer adipiscing elit, sed diam nonummy nibh euismod tincidunt ut laoreet dolore magna aliquam erat volutpat. Ut wisi enim ad minim veniam, quis nostrud exerci tation ullamcorper suscipit lobortis nisl ut aliquip ex ea commodo consequat.</p>
</div>
<div class="abs" style="left:96px;top:959px;width:190px">
  <h4 class="news-heading">Invitational Inter School Roller Skating Championship</h4>
  <p class="news-text" style="margin-top:6px">Lorem ipsum dolor sit amet, consectetuer adipiscing elit, sed diam nonummy nibh euismod tincidunt ut laoreet dolore magna aliquam erat volutpat.....</p>
</div>
<div class="abs" style="left:313px;top:959px;width:190px">
  <h4 class="news-heading">Investiture Ceremony held on 27th September 2013</h4>
  <p class="news-text" style="margin-top:6px">Lorem ipsum dolor sit amet, consectetuer adipiscing elit, sed diam nonummy nibh euismod tincidunt ut laoreet dolore magna aliquam erat volutpat.....</p>
</div>
<div class="btn btn-news abs">SEE ALL NEWS</div>

<h3 class="section-title abs" style="left:563px;top:787px">UPCOMING EVENTS</h3>
<div class="event-date abs" style="top:822px"><b>DEC</b><strong>10</strong></div>
<div class="abs" style="left:611px;top:820px;width:175px">
  <h4 class="news-heading">Lorem ipsum dolor sit amet, consectetuer adipiscing</h4>
  <p class="event-time">6:30pm</p>
  <p class="news-text" style="text-align:left">Duis autem vel eum iriure dolor in hendrerit in vulputate velit esse molestie consequat</p>
</div>
<div class="event-date abs" style="top:936px"><b>DEC</b><strong>24</strong></div>
<div class="abs" style="left:611px;top:934px;width:175px">
  <h4 class="news-heading">Lorem ipsum dolor sit amet, consectetuer adipiscing</h4>
  <p class="event-time">1:00pm</p>
  <p class="news-text" style="text-align:left">Duis autem vel eum iriure dolor in hendrerit in vulputate velit esse molestie consequat</p>
</div>
<div class="btn btn-events abs">SEE ALL EVENTS</div>

<footer class="site-footer abs"></footer>
<p class="copyright abs">© Copyright 2014, All rights reserved Kelmont Regional Academy.</p>
<div class="social abs" role="img" aria-label="Social media links"><i></i><i></i><i></i></div>

</body>
</html>
```